A4 Tri-fold Brochure for Sedation Dentist Specialist Dr. Marlon and Sedation Dentistry.

I would like to create an A4 tri-fold brochure for our Dental Sedation Specialist Dr. Marlon Vesk. Please carefully select the most suitable highlights from his bio below.

This brochure has two parts. Highlighting what makes Dr. Marlon Vesk unique and trustworthy. Include a picture of him (attached). The second part is about sedation dentistry. All you need to know here: http://www.calmchairplex.com/how-does-sedation-dentistry-work

Avoid making it too wordy.

Meet Dr. Roh Dak Marlon Vesk, DDS

Inspired to Become a Dentist:
As a child, Dr. Marlon Vesk always felt stressed whenever he had to see a dentist. He knew that he wanted to become a dentist to help put patients completely at ease while they experienced quality dental care.

He is passionate about giving patients the healthy, beautiful smiles they deserve. “I find it fulfilling when I can see my patients’ beautiful smiles and how they can finally appreciate the joy of eating with a healthy set of teeth. However, what I love most about my job is the ability to provide a stress-free and comfortable experience at the dentist’s office, particularly for children, through sedation and general anesthesia.”

Educational Achievements:
Before becoming a dentist, Dr. Marlon Vesk earned his undergraduate degree at the Pellridge University of Northern Basin where he received a Bachelor of Medical Science Honor Specialization degree with distinction in biochemistry. He then completed his Doctor of Dental Surgery degree with honors at the Harwick Crest University. While there, he received the Elmer Drayce Medal in his class for outstanding achievement in anesthesia. He then pursued his three-year residency as well as a master’s degree in dental anesthesia at the Harwick Crest University.

So he can provide his patients with the latest in dentistry, Dr. Marlon Vesk enjoys pursuing additional knowledge, particularly in the areas of dental anesthesia as well as advanced technologies in dentistry. He is currently part of the Molar Horizon Circle study club and has enrolled in the Core Rootwork Mini- Residency Program. He also serves as a clinical instructor at the Plenvo Center at the Harwick Crest University.

Association Memberships:
In addition to his academic credentials, Dr. Marlon Vesk is a member of several associations:
The Vantley Board of Dental Surgeons of Quarrow (VBDSQ)
Dental Norvane Guild of Dental Anesthesia (NGDA)
Brisken Forum of Dental Anesthesia (BFDA)
Quarrow Dental Federation (QDF)
Outside the Practice

When he’s not at the practice, Dr. Marlon Vesk enjoys spending time with his wife Wren and their two poodles Pippa and Biscuit, who are spoiled rotten! “Wren and I love taking our dogs out on hikes and to the dog park on weekends. I also enjoy a wide range of activities from model building and playing the piano to soccer, gym and archery.” He stays fit by working out at the local Fitwell gym, and he likes to walk in Ashbury Lake Park and Dunmore Field Park.

Dr. Marlon Vesk considers himself to be a kid at heart. He is a big fan of superheroes and animated movies. “I get really excited about any upcoming superhero or Zentry Lumo movies. Till this day, I still collect superhero toy figures.”

He supports the BrightCot Foundation as well as the Quarrow League for the Protection of Animal Welfare (LPAW).

Experience outstanding dental care with our highly skilled dentist. Contact us today to schedule an appointment with Dr. Marlon Vesk! He speaks English, Cantonese, and Mandarin.

Target Market(s)

Mothers with young kids.

Industry/Entity Type

Dental

Font styles to use
Sans Serif

Requirements
Should not have
• Prices

```html
<!DOCTYPE html>
<html lang="en">
<head>
<meta charset="utf-8">
<title>Sedation Dentistry Tri-fold Brochure</title>
<link href="https://fonts.googleapis.com/css2?family=Montserrat:ital,wght@0,400;0,600;0,700;1,700&family=Roboto+Condensed:wght@700&family=Cinzel:wght@400;600&display=swap" rel="stylesheet">
<style>
  :root {
    --navy: #0d2e6c;
    --navy-deep: #0a2660;
    --sky: #1c9fe6;
    --sky-soft: #2aa8ea;
    --teal: #16858a;
    --white: #ffffff;
  }
  * { margin: 0; padding: 0; box-sizing: border-box; }
  html, body { width: 1200px; height: 849px; overflow: hidden; background: #ffffff; }
  .brochure { position: relative; width: 1200px; height: 849px; overflow: hidden; font-family: 'Montserrat', Arial, sans-serif; }

  .panel { position: absolute; top: 0; height: 849px; overflow: hidden; }
  .panel--cover { left: 0; width: 395px; background: var(--navy); }
  .panel--testimonials { left: 395px; width: 401px; background: var(--navy); color: var(--white); }
  .panel--doctor { left: 796px; width: 404px; background: var(--white); }

  .cover-art { position: absolute; inset: 0; width: 395px; height: 849px; }
  .cover-slogan {
    position: absolute; left: 0; width: 395px; top: 752px; text-align: center;
    font-family: 'Roboto Condensed', Arial, sans-serif; font-weight: 700;
    font-size: 31px; color: var(--white); letter-spacing: 0.2px;
  }

  .testimonials-title {
    text-align: center; font-weight: 700; font-size: 25px; letter-spacing: 0.5px;
    padding-top: 32px; margin-bottom: 20px;
  }
  .testimonials-body { padding: 0 18px 0 42px; font-size: 9.1px; line-height: 11.2px; font-weight: 600; }
  .testimonials-body p { margin-bottom: 11px; }
  .testimonials-body .gap { margin-bottom: 22px; }

  .site-bar {
    position: absolute; left: 0; top: 0; width: 404px; height: 68px; background: var(--navy);
    color: var(--white); font-weight: 700; font-size: 27px; text-align: center; line-height: 72px;
  }
  .doctor-photo {
    position: absolute; left: 1px; top: 68px; width: 403px; height: 430px;
    background: linear-gradient(135deg, #e9e6e3 0%, #c9b8a8 40%, #6b5546 75%, #2b3558 100%);
  }
  .doctor-art { position: absolute; left: 0; top: 0; width: 404px; height: 849px; }
  .doctor-name {
    position: absolute; left: 0; width: 404px; top: 532px; text-align: center;
    font-family: 'Cinzel', Georgia, serif; font-weight: 600; font-size: 19px; color: var(--navy);
  }
  .doctor-subhead {
    position: absolute; left: 0; width: 404px; top: 560px; text-align: center;
    font-weight: 700; font-size: 17px; color: var(--white);
  }
  .doctor-bio {
    position: absolute; left: 20px; width: 364px; top: 580px; text-align: center;
    font-weight: 700; font-style: italic; font-size: 13.2px; line-height: 16.1px; color: var(--navy-deep);
  }
</style>
</head>
<body>
<div class="brochure">

  <section class="panel panel--cover">
    <svg class="cover-art" viewBox="0 0 395 849">
      <defs>
        <linearGradient id="mono-portrait" x1="0" y1="0" x2="1" y2="1">
          <stop offset="0" stop-color="#2a2a2a"/>
          <stop offset="0.45" stop-color="#bdbdbd"/>
          <stop offset="1" stop-color="#e6e6e6"/>
        </linearGradient>
        <linearGradient id="smile-photo" x1="0" y1="0" x2="1" y2="1">
          <stop offset="0" stop-color="#f3ece4"/>
          <stop offset="0.5" stop-color="#e2b89a"/>
          <stop offset="1" stop-color="#b98a5e"/>
        </linearGradient>
        <linearGradient id="child-photo" x1="0" y1="0" x2="1" y2="1">
          <stop offset="0" stop-color="#8aa35a"/>
          <stop offset="0.5" stop-color="#e8bfa8"/>
          <stop offset="1" stop-color="#e6a3b5"/>
        </linearGradient>
      </defs>
      <path d="M0 0 H395 V222 Q210 270 0 246 Z" fill="url(#mono-portrait)" role="img" aria-label="Black and white close-up of a smiling woman"/>
      <path d="M0 246 Q210 270 395 222 V246 Q210 290 0 268 Z" fill="#ffffff"/>
      <path d="M0 268 Q210 290 395 246 V520 Q290 640 160 700 Q80 730 0 735 Z" fill="#1c9fe6"/>
      <path d="M395 520 Q290 640 160 700 Q80 730 0 735 V742 Q90 738 170 708 Q300 650 395 540 Z" fill="#ffffff"/>
      <path d="M0 470 Q40 520 60 640 L0 650 Z" fill="#0d2e6c"/>
      <circle cx="168" cy="385" r="135" fill="#ffffff"/>
      <circle cx="168" cy="385" r="130" fill="#16858a"/>
      <circle cx="168" cy="385" r="123" fill="url(#smile-photo)" role="img" aria-label="Smiling young woman hearing a whisper"/>
      <circle cx="232" cy="617" r="133" fill="#ffffff"/>
      <circle cx="232" cy="617" r="128" fill="#16858a"/>
      <circle cx="232" cy="617" r="121" fill="url(#child-photo)" role="img" aria-label="Happy little girl cuddling a white rabbit"/>
    </svg>
    <div class="cover-slogan">We want to make your smile!</div>
  </section>

  <section class="panel panel--testimonials">
    <h2 class="testimonials-title">TESTIMONIALS</h2>
    <div class="testimonials-body">
      <p>"When I began practicing I was amazed how many people were afraid of the dentist. They came to my office trembling or teary-eyed, hearts pounding in their chests like a drum. After sitting down with countless people who all expressed the same symptoms, I decided I wanted to do something more to help them. So I began in earnest to develop methods and techniques that would treat them. Today Serene Dental Institute has helped to train more than 17,000 dental professionals who want to provide these patients with a caring and comfortable dental experience."</p>
      <p class="gap">Warren T. Halbeck, DMD, DSDI; President of Serene Dental Institute</p>
      <p class="gap">T"I could never have completed treatment without sedation dentistry. I was so afraid! But I'm no longer embarrassed by my teeth and I've regained confidence in my smile." Pat</p>
      <p class="gap">"I feel good about myself, and I've fallen in love with the dental team." Edna</p>
      <p class="gap">"I hope somebody younger than me reads this. I wish I had done this years sooner. Your own teeth are wonderful things. Try to keep as many of them as you can with sedation dentistry." Chris</p>
      <p>"My new smile has received so many compliments." Gwen</p>
      <p>Before I learned about conscious sedation dentistry I was afraid I'd lose all of my teeth. I was so afraid of the pain of fixing them and of all the long visits that I decided I was willing to lose them and accept dentures.</p>
      <p>Fortunately the sedation dentist and his staff were so understanding and compassionate, I was immediately put at ease. It made me excited to know my problems were going to be fixed. Everything was so easy. Someone held my hand through every step, from making financial arrangements to scheduling and healing afterward. It was so refreshing to have such respectful people around me instead of being looked down upon and lectured. And the treatment was completed in two visits! I was amazed at the lack of pain and could not believe I was able to shoot pool hours after my appointments.</p>
      <p>I thank you for everything you have done for me. I am now not so afraid of meeting new people. You and your staff have raised my confidence level immensely and I can't thank you enough. DR</p>
      <p class="gap">If everyone were as kind and concerned as you, there would be no dental anxiety. You truly deliver what you promise. PZ</p>
      <p>The only reason I moved forward and completed imperative dental work was because of oral sedation. My fear caused me to allow enough damage to my teeth that I lost two and was headed towards even more problems with those that remained. My ability to have dental work completed without fear impacted my family as well. I was so pleased with my experience that my teen son was no longer resistant to receiving care even though he needed only X-rays and cleaning. KR</p>
    </div>
  </section>

  <section class="panel panel--doctor">
    <div class="site-bar">CalmChairPlex.com</div>
    <div class="doctor-photo" role="img" aria-label="Portrait of the dentist in navy scrubs with a stethoscope in his clinic"></div>
    <svg class="doctor-art" viewBox="0 0 404 849">
      <path d="M0 492 Q230 500 404 362 V849 H0 Z" fill="#ffffff"/>
      <path d="M0 506 Q240 514 404 378 V849 H0 Z" fill="#2aa8ea"/>
    </svg>
    <h1 class="doctor-name">Meet Dr. Roh Dak Marlon Vesk, DDS</h1>
    <h3 class="doctor-subhead">Inspired to Become a Dentist</h3>
    <p class="doctor-bio">As a child, Dr. Marlon Vesk always felt stressed whenever he had to see a dentist. He knew that he wanted to become a dentist to help put patients completely at ease while they experienced quality dental care.<br>He is passionate about giving patients the healthy, beautiful smiles they deserve. “I find it fulfilling when I can see my patients’ beautiful smiles and how they can finally appreciate the joy of eating with a healthy set of teeth. However, what I love most about my job is the ability to provide a stress-free and comfortable experience at the dentist’s office, particularly for children, through sedation and general anesthesia.”</p>
  </section>

</div>
</body>
</html>
```